QuillMark Business Cards

I need a business card designed for QuillMark. To get an idea of what we do please visit https://formvault.example/para-creadores-3

```html
<!DOCTYPE html>
<html lang="en">
<head>
<meta charset="utf-8">
<title>QuillMark Business Cards</title>
<link rel="stylesheet" href="https://fonts.googleapis.com/css2?family=Montserrat:wght@300;400;500;700&display=swap">
<style>
  :root {
    --page: #3b3b3d;
    --card: #1f1f20;
    --white: #f2f2f2;
    --soft: #d9d9d9;
    --accent: #f0961e;
    --rule: #8a8a8a;
  }
  * { box-sizing: border-box; margin: 0; padding: 0; }
  html, body { width: 1200px; height: 1186px; overflow: hidden; }
  body {
    background: var(--page);
    font-family: "Montserrat", sans-serif;
    position: relative;
  }
  .card {
    position: absolute;
    left: 150px;
    width: 900px;
    height: 514px;
    background: var(--card);
    border-radius: 34px;
    overflow: hidden;
    box-shadow: 0 18px 40px rgba(0,0,0,.45);
  }
  .card--front { top: 56px; }
  .card--back { top: 616px; }

  .brand { position: absolute; display: flex; align-items: center; }
  .brand__square {
    border: 4px solid var(--accent);
    flex: none;
  }
  .brand__text { position: relative; }
  .brand__name {
    color: var(--white);
    font-weight: 400;
    letter-spacing: .32em;
    line-height: 1;
    display: block;
  }
  .brand__rule {
    position: absolute;
    right: 0;
    height: 1px;
    background: var(--rule);
  }
  .brand__tagline {
    color: var(--accent);
    font-weight: 500;
    letter-spacing: .38em;
    display: block;
  }

  .card--front .brand { left: 120px; top: 190px; gap: 44px; }
  .card--front .brand__square { width: 110px; height: 110px; }
  .card--front .brand__name { font-size: 46px; }
  .card--front .brand__rule { width: 150px; top: 62px; }
  .card--front .brand__tagline { font-size: 13px; margin-top: 22px; }

  .card--back .brand { left: 72px; top: 70px; gap: 30px; }
  .card--back .brand__square { width: 76px; height: 76px; }
  .card--back .brand__name { font-size: 32px; }
  .card--back .brand__rule { width: 105px; top: 44px; }
  .card--back .brand__tagline { font-size: 10px; margin-top: 15px; }

  .contact { position: absolute; left: 72px; top: 250px; }
  .contact__bar {
    position: absolute; left: -72px; top: 70px;
    width: 10px; height: 44px; background: var(--accent);
  }
  .contact__name {
    color: var(--accent); font-weight: 700; font-size: 28px;
  }
  .contact__role {
    color: var(--white); font-weight: 400; font-size: 17px; margin-top: 2px;
  }
  .contact__address {
    color: var(--soft); font-weight: 400; font-size: 17px;
    line-height: 1.3; margin-top: 24px; font-style: normal;
  }
  .contact__list { list-style: none; margin-top: 20px; }
  .contact__item {
    display: flex; align-items: center; gap: 14px;
    color: var(--soft); font-size: 17px; line-height: 1.55;
  }
  .contact__icon { width: 16px; height: 16px; fill: var(--accent); flex: none; }
</style>
</head>
<body>

<section class="card card--front" aria-label="Card front">
  <div class="brand">
    <span class="brand__square"></span>
    <div class="brand__text">
      <span class="brand__name">QUILLMARK</span>
      <span class="brand__rule"></span>
      <span class="brand__tagline">DIGITAL NOTARY</span>
    </div>
  </div>
</section>

<section class="card card--back" aria-label="Card back">
  <div class="brand">
    <span class="brand__square"></span>
    <div class="brand__text">
      <span class="brand__name">QUILLMARK</span>
      <span class="brand__rule"></span>
      <span class="brand__tagline">DIGITAL NOTARY</span>
    </div>
  </div>

  <div class="contact">
    <span class="contact__bar"></span>
    <h1 class="contact__name">Laura Brenner</h1>
    <p class="contact__role">CEO &amp; Founder</p>
    <address class="contact__address">Pol. Ind. Norvale, C/3 nº 12 2<br>2040&nbsp; Villa de Ormesa</address>
    <ul class="contact__list">
      <li class="contact__item">
        <svg class="contact__icon" viewBox="0 0 16 16"><path d="M3 1h3l1.5 4-2 1.3a9 9 0 0 0 4.2 4.2L11 8.5l4 1.5v3a2 2 0 0 1-2 2A12 12 0 0 1 1 3a2 2 0 0 1 2-2z"/></svg>
        955 41 27 80
      </li>
      <li class="contact__item">
        <svg class="contact__icon" viewBox="0 0 16 16"><path d="M1 3h14v1.5L8 9 1 4.5z"/><path d="M1 6.3 8 10.8l7-4.5V13H1z"/></svg>
        info@quillmark.example
      </li>
      <li class="contact__item">
        <svg class="contact__icon" viewBox="0 0 16 16"><circle cx="8" cy="8" r="6.5" fill="none" stroke="#f0961e" stroke-width="1.8"/><path d="M1.5 8h13M8 1.5c-3 3.5-3 9.5 0 13M8 1.5c3 3.5 3 9.5 0 13" fill="none" stroke="#f0961e" stroke-width="1.4"/></svg>
        www.quillmark.example
      </li>
    </ul>
  </div>
</section>

</body>
</html>
```